I need a business card design for a new company that will be doing consulting work around issues of cultural competency, and diversity and inclusion. I would like the design to be crisp and clear with bold but conservative colors and incorporate shades of blue

Target Market(s)

Small businesses, schools, non-profits

Industry/Entity Type

Consulting

Font styles to use
Serif
Sans Serif

Colors
0c5ba6
6b449b
3276b5
0292cd

Requirements
Must have
• A Morrow Venture (name of company)
• Lemlem Tavish
• CEO
• lemlem@amorrowventure.com
• (215)483-2756

```html
<!DOCTYPE html>
<html lang="en">
<head>
<meta charset="utf-8">
<title>A Morrow Venture — Business Card</title>
<link rel="stylesheet" href="https://fonts.googleapis.com/css2?family=Fira+Sans:wght@400;500&family=Fira+Sans+Condensed:wght@600&display=swap">
<style>
  :root {
    --page-bg: #e9ecef;
    --card-light: #5cbbe0;
    --card-mid: #2e97cf;
    --card-deep: #1a6cb0;
    --card-edge: #145ea3;
    --ink: #ffffff;
    --ink-soft: rgba(255, 255, 255, 0.85);
  }
  * { margin: 0; padding: 0; box-sizing: border-box; }
  html, body {
    width: 1200px;
    height: 1023px;
    overflow: hidden;
    background: var(--page-bg);
  }
  .canvas {
    position: relative;
    width: 1200px;
    height: 1023px;
    display: flex;
    align-items: center;
    justify-content: center;
  }
  .card {
    position: relative;
    width: 840px;
    height: 480px;
    border-radius: 22px;
    overflow: hidden;
    color: var(--ink);
    font-family: "Fira Sans", sans-serif;
    background:
      radial-gradient(ellipse 70% 80% at 42% 55%, var(--card-light) 0%, var(--card-mid) 45%, var(--card-deep) 85%, var(--card-edge) 100%);
    box-shadow: 0 14px 32px rgba(12, 91, 166, 0.28);
  }
  .company-name {
    position: absolute;
    left: 62px;
    top: 92px;
    font-size: 38px;
    font-weight: 400;
    letter-spacing: 3px;
    text-transform: uppercase;
  }
  .person {
    position: absolute;
    left: 132px;
    top: 238px;
    text-align: right;
  }
  .person-name {
    font-family: "Fira Sans Condensed", sans-serif;
    font-weight: 600;
    font-size: 40px;
    text-transform: uppercase;
    letter-spacing: 0.5px;
    line-height: 1;
  }
  .person-title {
    margin-top: 4px;
    font-size: 21px;
    letter-spacing: 1px;
    color: var(--ink-soft);
  }
  .divider {
    position: absolute;
    left: 426px;
    top: 226px;
    width: 2px;
    height: 66px;
    background: var(--ink-soft);
    transform: rotate(12deg);
  }
  .contact {
    position: absolute;
    left: 460px;
    top: 228px;
    list-style: none;
    font-size: 22px;
    line-height: 34px;
  }
  .contact li {
    display: flex;
    align-items: center;
    gap: 10px;
  }
  .contact svg {
    width: 16px;
    height: 16px;
    flex: none;
  }
</style>
</head>
<body>
  <main class="canvas">
    <article class="card">
      <h1 class="company-name">A Morrow Venture</h1>
      <div class="person">
        <p class="person-name">Lemlem Tavish</p>
        <p class="person-title">CEO</p>
      </div>
      <span class="divider" aria-hidden="true"></span>
      <ul class="contact">
        <li>
          <svg viewBox="0 0 16 16" aria-hidden="true"><path d="M4 1.5 6.2 4 5 5.6c.8 2 2.4 3.6 4.4 4.4L11 8.8l2.5 2.2-1.2 2.5C7 13 3 9 2.5 3.6Z" fill="#fff"/></svg>
          <span>(215)483-2756</span>
        </li>
        <li>
          <svg viewBox="0 0 16 16" aria-hidden="true"><rect x="1.5" y="3.5" width="13" height="9" fill="none" stroke="#fff" stroke-width="1.4"/><path d="M1.5 3.5 8 9l6.5-5.5" fill="none" stroke="#fff" stroke-width="1.4"/></svg>
          <span>lemlem@amorrowventure.com</span>
        </li>
      </ul>
    </article>
  </main>
</body>
</html>
```